Ad Banner for knowledge management portal - Promote Knowledge Submission

This banner is used in knowledge management web site.

1. Banner size: 940x380
2. Business background: Provides maintenance, design and engineering, construction, machinery operation, material procurement and production management services for petrochemical and refinery business
3. We would like to see designs that
- Promote the benefits of sharing "Lesson Learned".
- Use the keyword "I will do it better if I have to do it again"
- Promote employees to submit "Lesson Learned". It is a lesson learned from work, submitted using a predefined form template.
- Promote a campaign that will give out souvenir for all employees who submit "Lesson Learned"
- Has the message "Click here to learn more about Lesson Learned"

Requirements
Must have
• Must have a picture of technician examining machine or equipments (using cartoon character)
Should not have
• Should not include picture of real people in the design

```html
<!DOCTYPE html>
<html lang="en">
<head>
<meta charset="utf-8">
<title>Lesson Learned – Share Your Knowledge</title>
<link rel="stylesheet" href="https://fonts.googleapis.com/css2?family=Bangers&display=swap">
<style>
  :root {
    --bg-centre: #8a8240;
    --bg-mid: #5e5828;
    --bg-edge: #1f1c0c;
    --steel-light: #e4e6e8;
    --steel-mid: #b9bcc0;
    --steel-dark: #8d9095;
    --band-dark: #6f7378;
    --frame-light: #f2f3f4;
    --frame-dark: #8a8d91;
    --rivet-light: #ffffff;
    --rivet-dark: #5c5f63;
    --headline: #ff9a12;
    --headline-edge: #3a1c00;
    --footer-text: #8fc0ff;
    --footer-edge: #0d1a33;
    --icon-fill: #8a8e93;
    --scene-machine: #5c5e62;
    --scene-steel: #8e9088;
    --scene-lamp: #8fa04a;
  }
  * { margin: 0; padding: 0; box-sizing: border-box; }
  html, body { width: 1200px; height: 750px; overflow: hidden; }
  body {
    position: relative;
    background: radial-gradient(ellipse 70% 65% at 50% 48%, var(--bg-centre) 0%, var(--bg-mid) 55%, var(--bg-edge) 100%);
    font-family: "Bangers", "Comic Sans MS", cursive;
  }
  .banner {
    position: absolute; left: 130px; top: 185px; width: 940px; height: 380px;
    background:
      repeating-linear-gradient(115deg, rgba(255,255,255,.18) 0 2px, rgba(0,0,0,.05) 2px 5px, rgba(255,255,255,.08) 5px 7px),
      linear-gradient(135deg, var(--steel-mid) 0%, var(--steel-light) 45%, var(--steel-mid) 70%, var(--steel-dark) 100%);
    box-shadow: 0 6px 14px rgba(0,0,0,.6), inset 0 0 0 1px rgba(255,255,255,.5);
  }
  .banner__footer {
    position: absolute; left: 0; right: 0; bottom: 0; height: 58px;
    background:
      repeating-linear-gradient(115deg, rgba(255,255,255,.12) 0 2px, rgba(0,0,0,.06) 2px 5px),
      linear-gradient(180deg, var(--band-dark), var(--steel-dark) 50%, var(--band-dark));
    border-top: 2px solid #4c4f53;
    box-shadow: inset 0 2px 0 rgba(255,255,255,.35);
  }
  .technician-scene {
    position: absolute; left: 245px; top: 70px; width: 460px; height: 252px;
    border-radius: 14px;
    background: linear-gradient(90deg,
      rgba(92,94,98,0) 0%,
      var(--scene-machine) 18%,
      var(--scene-steel) 48%,
      var(--scene-lamp) 78%,
      rgba(143,160,74,0) 100%);
    opacity: .75;
    -webkit-mask-image: linear-gradient(180deg, transparent 0%, #000 30%, #000 100%);
            mask-image: linear-gradient(180deg, transparent 0%, #000 30%, #000 100%);
  }
  .rivet {
    position: absolute; width: 24px; height: 24px; border-radius: 50%;
    background: radial-gradient(circle at 35% 30%, var(--rivet-light), #c3c6ca 45%, var(--rivet-dark) 100%);
    box-shadow: 0 1px 3px rgba(0,0,0,.6);
  }
  .rivet--tl { left: 8px; top: 10px; }
  .rivet--tr { right: 6px; top: 10px; }
  .rivet--bl { left: 8px; bottom: 16px; }
  .rivet--br { right: 8px; bottom: 16px; }
  .feature { position: absolute; top: 27px; width: 300px; text-align: center; }
  .feature--submit { left: -5px; }
  .feature--motto { left: 320px; }
  .feature--learn { left: 645px; }
  .feature__frame {
    position: relative; margin: 0 auto; width: 170px; height: 170px;
    background: linear-gradient(135deg, var(--frame-light), var(--steel-mid) 50%, var(--frame-dark));
    box-shadow: 0 3px 8px rgba(0,0,0,.55), inset 0 0 0 2px rgba(0,0,0,.15);
    padding: 20px;
  }
  .feature__frame::before {
    content: ""; position: absolute; width: 7px; height: 7px; border-radius: 50%;
    background: radial-gradient(circle at 35% 30%, #fff, #777);
    top: 6px; left: 6px; box-shadow: 151px 0 0 #999, 0 151px 0 #999, 151px 151px 0 #999;
  }
  .feature__art { width: 130px; height: 130px; box-shadow: inset 0 0 0 2px rgba(0,0,0,.4); }
  .feature__art--souvenir { background: linear-gradient(140deg, #5a3424, #8a6a4a 40%, #4b4a50 70%, #c25a3a); }
  .feature__art--wiring { background: radial-gradient(circle at 50% 45%, #c97a3a, #8a4218 70%, #5a2a10); }
  .feature__art--gears { background: radial-gradient(circle at 40% 45%, #6b4a34, #3b2f28 60%, #1e1a18); }
  .feature__icon { display: block; margin: 14px auto 0; width: 48px; height: 48px; }
  .feature__caption {
    margin-top: 9px; font-size: 21px; line-height: 22px; letter-spacing: .6px;
    color: var(--headline);
    text-shadow: -1px -1px 0 var(--headline-edge), 1px -1px 0 var(--headline-edge), -1px 1px 0 var(--headline-edge), 1px 1px 0 var(--headline-edge), 0 2px 2px rgba(0,0,0,.5);
  }
  .banner__tagline {
    position: absolute; left: 0; right: 0; bottom: 4px; text-align: center;
    font-size: 20.5px; line-height: 23px; letter-spacing: .8px; color: var(--footer-text);
    text-shadow: -1px -1px 0 var(--footer-edge), 1px -1px 0 var(--footer-edge), -1px 1px 0 var(--footer-edge), 1px 1px 0 var(--footer-edge);
    padding-right: 30px;
  }
</style>
</head>
<body>
  <section class="banner">
    <div class="technician-scene" role="img" aria-label="Cartoon technician examining a control machine and an industrial drill press in a workshop"></div>
    <div class="banner__footer"></div>
    <span class="rivet rivet--tl"></span>
    <span class="rivet rivet--tr"></span>
    <span class="rivet rivet--bl"></span>
    <span class="rivet rivet--br"></span>

    <div class="feature feature--submit">
      <div class="feature__frame"><div class="feature__art feature__art--souvenir" role="img" aria-label="Assorted souvenirs: cowboy hat, rope, dice and gift box"></div></div>
      <svg class="feature__icon" viewBox="0 0 48 48" aria-hidden="true">
        <circle cx="24" cy="24" r="22" fill="#eef0f2" stroke="#7d8085" stroke-width="2"/>
        <circle cx="24" cy="24" r="17" fill="var(--icon-fill)"/>
        <rect x="14" y="17" width="20" height="14" fill="#fff"/>
        <path d="M14 17 L24 25 L34 17" fill="none" stroke="#8a8e93" stroke-width="1.6"/>
      </svg>
      <p class="feature__caption">Submit your lesson learned today<br>and get a cool souvenir</p>
    </div>

    <div class="feature feature--motto">
      <div class="feature__frame"><div class="feature__art feature__art--wiring" role="img" aria-label="Tangle of copper wires on a terminal board"></div></div>
      <svg class="feature__icon" viewBox="0 0 48 48" aria-hidden="true">
        <circle cx="24" cy="24" r="22" fill="#eef0f2" stroke="#7d8085" stroke-width="2"/>
        <circle cx="24" cy="24" r="17" fill="var(--icon-fill)"/>
        <ellipse cx="24" cy="23" rx="10" ry="8" fill="#fff"/>
        <path d="M18 28 L16 34 L23 30 Z" fill="#fff"/>
      </svg>
      <p class="feature__caption">I will do it better<br>if I have to do it again...</p>
    </div>

    <div class="feature feature--learn">
      <div class="feature__frame"><div class="feature__art feature__art--gears" role="img" aria-label="Rusty gears and chain mechanism"></div></div>
      <svg class="feature__icon" viewBox="0 0 48 48" aria-hidden="true">
        <circle cx="24" cy="24" r="22" fill="#eef0f2" stroke="#7d8085" stroke-width="2"/>
        <circle cx="24" cy="24" r="17" fill="var(--icon-fill)"/>
        <path d="M14 24 L34 15 L28 34 L24 27 Z" fill="#fff"/>
        <path d="M24 27 L34 15" stroke="#8a8e93" stroke-width="1.2"/>
      </svg>
      <p class="feature__caption">Click here to learn more<br>about lesson learned</p>
    </div>

    <p class="banner__tagline">Share your knowledge, technics, experience in maintenance and<br>engineering in machines and equipments using lesson learned</p>
  </section>
</body>
</html>
```